Powepoint template for an investment group

Need high end clear clean concise creative luxurious

Have royal clients
High end/billionaire investors

Using ross gold logo can be creative
Must habe page numbers
Logo preference header top right
Page number footer bottom right

The first page of the ppt maybe a big block of dark grey and oberi investment group written on the front page in rose gold

Target Market(s)

Investors at a high level

Requirements
Must have
• Luxury feel

```html
<!DOCTYPE html>
<html lang="en">
<head>
<meta charset="utf-8">
<title>Oberi Investment Group – Presentation Template</title>
<link rel="stylesheet" href="https://fonts.googleapis.com/css2?family=Montserrat:wght@300;400;600;700;800&display=swap">
<style>
:root{
  --paper:#f1f1f1;
  --ink:#121213;
  --charcoal:#26272a;
  --slate:#3b3f46;
  --gold:#e9a43c;
  --gold-deep:#c57f22;
  --light:#e9e9e9;
  --muted:#b9b9b9;
  --white:#ffffff;
}
*{box-sizing:border-box;margin:0;padding:0}
html,body{width:1200px;height:4275px;overflow:hidden;background:var(--paper)}
body{position:relative;font-family:"Montserrat",sans-serif;color:var(--light)}
.slide{position:absolute;width:554px;height:312px;overflow:hidden;background:var(--ink)}
.slide.cover{width:552px;height:311px}
.col-l{left:32px}.col-r{left:616px}
.photo{position:absolute;inset:0}
.shade{position:absolute;inset:0;background:linear-gradient(90deg,rgba(10,10,12,.82),rgba(10,10,12,.55) 55%,rgba(10,10,12,.7))}
.ph-city{background:linear-gradient(180deg,#6d7a8c 0%,#3c4656 45%,#1c222b 100%)}
.ph-tower{background:linear-gradient(160deg,#8b98aa 0%,#4a5567 50%,#1f242c 100%)}
.ph-office{background:linear-gradient(135deg,#5e5a55 0%,#3a3633 50%,#1a1918 100%)}
.ph-warm{background:linear-gradient(135deg,#7a6550 0%,#4a3c30 55%,#1d1814 100%)}
.ph-sunset{background:linear-gradient(180deg,#b58a5c 0%,#5b4c42 45%,#1c1a1a 100%)}
.ph-cool{background:linear-gradient(135deg,#c9d3dc 0%,#8c9aa8 60%,#5f6c78 100%)}
.ph-grey{background:linear-gradient(135deg,#8d8d8d 0%,#5b5b5b 55%,#2e2e2e 100%)}
.brand{position:absolute;top:20px;right:24px;color:var(--white);font-weight:600;font-size:8px;letter-spacing:.4px;line-height:1;text-transform:uppercase;white-space:nowrap}
.brand.big{top:50%;left:50%;right:auto;transform:translate(-50%,-50%);font-size:24px;letter-spacing:.6px}
.brand.mid{left:50%;right:auto;transform:translateX(-50%);font-size:18px}
.title{position:absolute;font-weight:700;font-size:10px;color:var(--white);letter-spacing:.3px}
.title::before{content:"";position:absolute;left:0;top:-6px;width:16px;height:1.5px;background:var(--gold)}
.title em,.gold{color:var(--gold);font-style:normal}
.txt{position:absolute;font-size:5.5px;line-height:1.55;color:var(--light)}
.txt b{display:block;font-size:6px;color:var(--white);margin-bottom:1px}
.foot{position:absolute;left:30px;bottom:12px;font-size:4.5px;color:var(--muted)}
.num{position:absolute;right:30px;bottom:12px;font-size:5px;color:var(--muted)}
.rule{position:absolute;left:0;right:0;bottom:4px;height:1.5px;background:linear-gradient(90deg,transparent,var(--gold) 20%,var(--gold) 80%,transparent)}
.btn{position:absolute;height:10px;background:var(--gold);color:var(--white);font-size:4.5px;text-align:center;line-height:10px;border-radius:1px}
.card{position:absolute;background:rgba(30,31,34,.9)}
.tile{position:absolute;width:62px;height:62px;background:rgba(24,26,30,.85);border:1px solid rgba(233,164,60,.35);text-align:center;font-size:5.5px;padding-top:40px}
.tile svg{position:absolute;left:21px;top:14px}
.dots{letter-spacing:2px;color:var(--white);font-size:8px}
table.grid{position:absolute;border-collapse:collapse;font-size:5px}
table.grid td,table.grid th{padding:0 6px;height:18px;text-align:left;border-bottom:1px solid rgba(255,255,255,.25);color:var(--light);font-weight:400}
table.grid th{background:var(--gold);color:var(--white);font-weight:600;height:14px}
table.grid tr:nth-child(even) td{background:rgba(233,164,60,.18)}
</style>
</head>
<body>

<!-- 01 Cover -->
<section class="slide cover" style="left:324px;top:51px;background:linear-gradient(180deg,#1b1b1d,#0c0c0d)">
  <div class="brand big">Oberi Investment Group</div>
  <i class="rule" style="bottom:42px;left:40px;right:40px;height:1px"></i>
</section>

<!-- 02 Title dark -->
<section class="slide col-l" style="top:394px;background:linear-gradient(135deg,#2a2b2e,#101011 60%,#1e1f21)">
  <svg width="554" height="312" style="position:absolute;inset:0">
    <line x1="170" y1="0" x2="554" y2="150" stroke="#e9a43c" stroke-width=".8"/>
    <line x1="0" y1="270" x2="230" y2="312" stroke="#e9a43c" stroke-width=".8"/>
    <polygon points="330,0 554,0 554,110" fill="rgba(255,255,255,.05)"/>
  </svg>
  <div class="brand big" style="left:45%">Oberi Investment Group</div>
</section>

<!-- 03 Presentation title -->
<section class="slide col-r" style="top:394px">
  <div class="photo ph-city" role="img" aria-label="City skyline with skyscrapers at dusk"></div>
  <div class="shade" style="background:rgba(15,18,24,.45)"></div>
  <div class="brand mid" style="top:96px">Oberi Investment Group</div>
  <div style="position:absolute;top:150px;width:100%;text-align:center;font-weight:800;font-size:18px;color:var(--white)">PRESENTATION <span class="gold">GOES HERE</span></div>
  <div style="position:absolute;top:176px;width:100%;text-align:center;font-size:11px;font-weight:300">Subtitle Presentation</div>
  <p class="foot" style="left:190px">© 2022 Copyright Oberi Investment Group - All Rights Reserved</p><span class="num">01</span><i class="rule"></i>
</section>

<!-- 04 Section -->
<section class="slide col-l" style="top:735px">
  <div class="photo ph-tower" role="img" aria-label="Glass office towers seen from below"></div>
  <div class="shade"></div>
  <div class="brand">Oberi Investment Group</div>
  <div style="position:absolute;left:30px;top:118px;font-size:6px">Section</div>
  <div class="title" style="left:30px;top:128px;text-transform:uppercase">Lorem <em>Ipsum</em></div>
  <p class="txt" style="left:30px;top:146px;width:180px">Lorem ipsum dolor sit amet, consectetuer adipiscing elit, sed diam nonummy nibh euismod tincidunt ut laoreet dolore magna aliquam erat volutpat. Ut wisi enim ad minim veniam, quis nostrud exerci tation ullamcorper suscipit lobortis nisl ut aliquip ex ea.</p>
  <p class="txt" style="left:298px;top:78px;width:200px"><b>Lorem Ipsum</b>Lorem ipsum dolor sit amet consectetuer adipiscing elit sed diam nonummy nibh euismod tincidunt ut laoreet</p>
  <p class="txt" style="left:290px;top:120px;width:215px;padding:4px 8px;border:1px solid var(--gold);border-radius:3px"><b>Lorem Ipsum</b>Lorem ipsum dolor sit amet consectetuer adipiscing elit sed diam nonummy nibh euismod tincidunt ut laoreet</p>
  <p class="txt" style="left:298px;top:172px;width:200px"><b>Lorem Ipsum</b>Lorem ipsum dolor sit amet consectetuer adipiscing elit sed diam nonummy nibh euismod tincidunt ut laoreet</p>
  <p class="txt" style="left:298px;top:222px;width:200px"><b>Lorem Ipsum</b>Lorem ipsum dolor sit amet consectetuer adipiscing elit sed diam nonummy nibh euismod tincidunt ut laoreet</p>
  <p class="foot">© 2022 Copyright Oberi Investment Group - All Rights Reserved</p><span class="num">02</span><i class="rule"></i>
</section>

<!-- 05 Team -->
<section class="slide col-r" style="top:735px">
  <div class="photo ph-office" role="img" aria-label="Business team standing together in an office"></div>
  <div class="shade"></div>
  <div class="brand">Oberi Investment Group</div>
  <div class="title" style="left:30px;top:130px">LOREM <em>IPSUM</em></div>
  <p class="txt" style="left:30px;top:146px;width:200px">Lorem ipsum dolor sit amet, consectetuer adipiscing elit, sed diam nonummy nibh euismod tincidunt ut laoreet dolore magna aliquam erat volutpat. Ut wisi enim ad minim veniam, quis nostrud exerci tation ullamcorper suscipit lobortis nisl ut aliquip ex ea.</p>
  <div style="position:absolute;left:258px;top:98px;width:272px;height:128px;background:var(--white);padding:4px;display:grid;grid-template-columns:1fr 1fr;gap:4px">
    <div class="ph-office" role="img" aria-label="Two colleagues talking"></div>
    <div class="ph-grey" role="img" aria-label="Team meeting around a table"></div>
    <div class="ph-warm" role="img" aria-label="Professionals in discussion"></div>
    <div class="ph-cool" role="img" aria-label="Businesswoman at work"></div>
  </div>
  <p class="foot">© 2022 Copyright Oberi Investment Group - All Rights Reserved</p><span class="num">03</span><i class="rule"></i>
</section>

<!-- 06 Two columns -->
<section class="slide col-l" style="top:1076px">
  <div class="photo ph-warm" role="img" aria-label="Dartboard with dart in the bullseye"></div>
  <div class="shade"></div>
  <div class="brand">Oberi Investment Group</div>
  <div class="title" style="left:30px;top:55px">LOREM <em>IPSUM</em></div>
  <p class="txt" style="left:30px;top:82px;width:230px"><b class="gold">Lorem Ipsum Dolor Sit</b>Lorem ipsum dolor sit amet, consectetuer adipiscing elit, sed diam nonummy nibh euismod tincidunt ut laoreet dolore magna aliquam erat volutpat. Ut wisi enim ad minim veniam, quis nostrud exerci tation ullamcorper suscipit lobortis nisl ut aliquip ex ea commodo consequat. Duis autem vel eum iriure dolor in hendrerit in vulputate velit esse molestie consequat, vel illum dolore eu feugiat nulla facilisis at vero eros et accumsan et iusto odio dignissim qui blandit praesent luptatum zzril delenit augue duis dolore te feugait nulla facilisi.<br><br>Lorem ipsum dolor sit amet, cons ectet adipiscing elit, sed diam nonummy nibh euismod tincidunt ut laoreet dolore magna aliquam erat volutpat. Ut wisi enim ad minim veniam, quis nostrud exerci tation ullamcorper suscipit lobortis nisl ut aliquip ex ea commodo consequat.</p>
  <p class="txt" style="left:296px;top:82px;width:230px"><b class="gold">Lorem Ipsum Dolor Sit</b>Lorem ipsum dolor sit amet, consectetuer adipiscing elit, sed diam nonummy nibh euismod tincidunt ut laoreet dolore magna aliquam erat volutpat. Ut wisi enim ad minim veniam, quis nostrud exerci tation ullamcorper suscipit lobortis nisl ut aliquip ex ea commodo consequat. Duis autem vel eum iriure dolor in hendrerit in vulputate velit esse molestie consequat, vel illum dolore eu feugiat nulla facilisis at vero eros et accumsan et iusto odio dignissim qui blandit praesent luptatum zzril delenit augue duis dolore te feugait nulla facilisi.</p>
  <p class="foot">© 2022 Copyright Oberi Investment Group - All Rights Reserved</p><span class="num">04</span><i class="rule"></i>
</section>

<!-- 07 White bullets -->
<section class="slide col-r" style="top:1076px;background:var(--white)">
  <div class="photo ph-cool" style="left:296px" role="img" aria-label="Hands holding a tablet and pen over a desk"></div>
  <div class="brand">Oberi Investment Group</div>
  <div class="title" style="left:30px;top:55px;color:var(--ink)">LOREM <em>IPSUM</em></div>
  <p class="txt" style="left:30px;top:88px;width:240px;color:#333">Lorem ipsum dolor sit ametconsec adipiscing elit, sed diam nonummy nibh euismod tincidunt ut laoreet dolore magna aliquam erat volutpat. Ut wisi enim ad minim veniam, quis nostrud exerci tation ullamcorper suscipit lobortis nisl ut aliquip ex ea commodo consequat. Duis autem vel eum iriure dolor in hendrerit in vulput velit esse molestie consequat, vel illum dolore eu feugiat nulla facilisis.</p>
  <svg width="10" height="110" style="position:absolute;left:30px;top:160px"><g fill="#e9a43c"><circle cx="4" cy="4" r="3"/><circle cx="4" cy="31" r="3"/><circle cx="4" cy="58" r="3"/><circle cx="4" cy="85" r="3"/></g></svg>
  <p class="txt" style="left:42px;top:160px;width:220px;color:#333;line-height:1.5">Lorem ipsum dolor sit ametconsec adipiscing elit, sed diam nonummy nibh euismod tincidunt ut laoreet dolore aliquam<br><br>Lorem ipsum dolor sit ametconsec adipiscing elit, sed diam nonummy nibh euismod tincidunt ut laoreet dolore aliquam<br><br>Lorem ipsum dolor sit ametconsec adipiscing elit, sed diam nonummy nibh euismod tincidunt ut laoreet dolore aliquam<br><br>Lorem ipsum dolor sit ametconsec adipiscing elit, sed diam nonummy nibh euismod tincidunt ut laoreet dolore aliquam</p>
  <p class="foot" style="color:#555">© 2022 Copyright Oberi Investment Group - All Rights Reserved</p><i class="rule" style="right:260px"></i>
</section>

<!-- 08 Full text -->
<section class="slide col-l" style="top:1417px">
  <div class="photo ph-sunset" role="img" aria-label="Silhouettes of business people against a window"></div>
  <div class="shade" style="background:rgba(10,12,18,.55)"></div>
  <div class="brand">Oberi Investment Group</div>
  <div class="title" style="left:30px;top:55px">LOREM <em>IPSUM</em></div>
  <p class="txt" style="left:30px;top:92px;width:494px">Lorem ipsum dolor sit amet, consectetuer adipiscing elit, sed diam nonummy nibh euismod tincidunt ut laoreet dolore magna aliquam erat volutpat. Ut wisi enim ad minim veniam, quis nostrud exerci tation ullamcorper suscipit lobortis nisl ut aliquip ex ea commodo consequat. Duis autem vel eum iriure dolor in hendrerit in vulputate velit esse molestie consequat, vel illum dolore eu feugiat nulla facilisis at vero eros et accumsan et iusto odio dignissim qui blandit.<br><br>Lorem ipsum dolor sit amet, consectetuer adipiscing elit, sed diam nonummy nibh euismod tincidunt ut laoreet dolore magna aliquam erat volutpat. Ut wisi enim ad minim veniam, quis nostrud exerci tation ullamcorper suscipit lobortis nisl ut aliquip ex ea commodo consequat.<br><br>Lorem ipsum dolor sit amet, consectetuer adipiscing elit, sed diam nonummy nibh euismod tincidunt ut laoreet dolore magna aliquam erat volutpat. Ut wisi enim ad minim veniam, quis nostrud exerci tation ullamcorper suscipit lobortis nisl ut aliquip ex ea commodo consequat. Duis autem vel eum iriure dolor in hendrerit in vulputate velit esse molestie consequat, vel illum dolore eu feugiat nulla facilisis at vero eros et accumsan.<br><br>Lorem ipsum dolor sit amet, consectetuer adipiscing elit, sed diam nonummy nibh euismod tincidunt ut laoreet dolore magna aliquam erat volutpat. Ut wisi enim ad minim veniam, quis nostrud exerci tation ullamcorper suscipit lobortis nisl ut aliquip ex ea commodo consequat.</p>
  <p class="foot">© 2022 Copyright Oberi Investment Group - All Rights Reserved</p><span class="num">06</span><i class="rule"></i>
</section>

<!-- 09 Image left, gallery -->
<section class="slide col-r" style="top:1417px;background:linear-gradient(180deg,#1c1c1e,#2a2a2d)">
  <div class="photo ph-warm" style="right:372px" role="img" aria-label="Team members joining hands over a table"></div>
  <div class="brand">Oberi Investment Group</div>
  <div class="title" style="left:208px;top:80px">LOREM <em>IPSUM</em></div>
  <p class="txt" style="left:208px;top:100px;width:320px">Lorem ipsum dolor sit amet, consectetuer adipiscing elit, sed diam nonummy nibh euismod tincidunt ut laoreet dolore magna aliquam erat volutpat. Ut wisi enim ad minim veniam, quis nostrud exerci tation ullamcorper suscipit lobortis nisl ut aliquip ex ea commodo consequat. Duis autem vel eum iriure dolor in hendrerit in vulputate velit esse molestie consequat, vel illum dolore eu feugiat nulla facilisis at vero eros.</p>
  <div class="ph-office" style="position:absolute;left:208px;top:168px;width:74px;height:74px" role="img" aria-label="Colleagues shaking hands"></div>
  <div class="ph-cool" style="position:absolute;left:288px;top:168px;width:74px;height:74px" role="img" aria-label="Laptop and documents on a desk"></div>
  <div class="ph-tower" style="position:absolute;left:368px;top:168px;width:74px;height:74px" role="img" aria-label="Business person reviewing a tablet"></div>
  <div class="ph-grey" style="position:absolute;left:448px;top:168px;width:74px;height:74px" role="img" aria-label="Businessman in a suit"></div>
  <p class="foot">© 2022 Copyright Oberi Investment Group - All Rights Reserved</p><span class="num">07</span><i class="rule"></i>
</section>

<!-- 10 Grid items -->
<section class="slide col-l" style="top:1758px">
  <div class="photo ph-tower" role="img" aria-label="Skyline viewed through office windows"></div>
  <div class="shade"></div>
  <div class="brand">Oberi Investment Group</div>
  <div class="title" style="left:30px;top:55px">LOREM <em>IPSUM</em></div>
  <p class="txt" style="left:30px;top:78px;width:125px">Lorem ipsum dolor sit ametconsec adipiscing elit, sed diam nonummy nibh euismod tincidunt ut laoreet dolore magna aliquam erat volutpat. Ut wisi enim ad minim veniam, quis nostrud exerci tation ullamcorper suscipit lobortis nisl ut aliquip ex ea commodo consequat. Duis autem vel eum iriure dolor in hendrerit in vulputate velit esse molestie consequat, vel illum dolore eu feugiat nulla facilisis at vero eros et accumsan et iusto odio dignissim.<br><br><span class="gold">Lorem ipsum dolor sit amet, cons ectet adipiscing elit, sed diam nonummy nibh.</span></p>
  <p class="txt" style="left:198px;top:88px;width:140px"><b class="gold">Lorem Ipsum Dolor Sit</b>Lorem ipsum dolor sit amet, unt consectetuer adipiscing elit sed diam nonummy is euismod tincidunt ut laoreet</p>
  <p class="txt" style="left:372px;top:88px;width:140px"><b class="gold">Lorem Ipsum Dolor Sit</b>Lorem ipsum dolor sit amet, unt consectetuer adipiscing elit sed diam nonummy is euismod tincidunt ut laoreet</p>
  <p class="txt" style="left:198px;top:148px;width:140px"><b class="gold">Lorem Ipsum Dolor Sit</b>Lorem ipsum dolor sit amet, unt consectetuer adipiscing elit sed diam nonummy is euismod tincidunt ut laoreet</p>
  <p class="txt" style="left:364px;top:142px;width:156px;padding:5px 8px;border:1px solid var(--gold);border-radius:2px"><b class="gold">Lorem Ipsum Dolor Sit</b>Lorem ipsum dolor sit amet, unt consectetuer adipiscing elit sed diam nonummy is euismod tincidunt ut laoreet</p>
  <p class="txt" style="left:198px;top:208px;width:140px"><b class="gold">Lorem Ipsum Dolor Sit</b>Lorem ipsum dolor sit amet, unt consectetuer adipiscing elit sed diam nonummy is euismod tincidunt ut laoreet</p>
  <p class="txt" style="left:372px;top:208px;width:140px"><b class="gold">Lorem Ipsum Dolor Sit</b>Lorem ipsum dolor sit amet, unt consectetuer adipiscing elit sed diam nonummy is euismod tincidunt ut laoreet</p>
  <p class="foot">© 2022 Copyright Oberi Investment Group - All Rights Reserved</p><span class="num">08</span><i class="rule"></i>
</section>

<!-- 11 Four images with buttons -->
<section class="slide col-r" style="top:1758px;background:linear-gradient(180deg,#151516,#3a3a3c)">
  <div class="brand">Oberi Investment Group</div>
  <div class="title" style="left:0;right:0;top:50px;text-align:center">LOREM <em>IPSUM</em></div>
  <p class="txt" style="left:160px;top:66px;width:234px;text-align:center">Lorem ipsum dolor sit amet, consectetuer adipiscing elit, sed diam nonummy nibh euismod tincidunt ut laoreet dolorerrum</p>
  <div class="ph-cool" style="position:absolute;left:30px;top:94px;width:115px;height:74px" role="img" aria-label="Hand touching a digital screen"></div>
  <div class="ph-tower" style="position:absolute;left:156px;top:94px;width:115px;height:74px" role="img" aria-label="Handshake between partners"></div>
  <div class="ph-cool" style="position:absolute;left:282px;top:94px;width:115px;height:74px" role="img" aria-label="Finger pointing at financial chart"></div>
  <div class="ph-sunset" style="position:absolute;left:408px;top:94px;width:115px;height:74px" role="img" aria-label="Crowd of people in a hall"></div>
  <p class="txt" style="left:30px;top:176px;width:115px;text-align:center">Lorem ipsum dolor sit ameti consectet adipiscing elit, sed diam nonummy nibh euismod</p>
  <p class="txt" style="left:156px;top:176px;width:115px;text-align:center">Lorem ipsum dolor sit ameti consectet adipiscing elit, sed diam nonummy nibh euismod</p>
  <p class="txt" style="left:282px;top:176px;width:115px;text-align:center">Lorem ipsum dolor sit ameti consectet adipiscing elit, sed diam nonummy nibh euismod</p>
  <p class="txt" style="left:408px;top:176px;width:115px;text-align:center">Lorem ipsum dolor sit ameti consectet adipiscing elit, sed diam nonummy nibh euismod</p>
  <span class="btn" style="left:58px;top:200px;width:60px">Lorem ipsum</span>
  <span class="btn" style="left:184px;top:200px;width:60px">Lorem ipsum</span>
  <span class="btn" style="left:310px;top:200px;width:60px">Lorem ipsum</span>
  <span class="btn" style="left:436px;top:200px;width:60px">Lorem ipsum</span>
  <p class="foot">© 2022 Copyright Oberi Investment Group - All Rights Reserved</p><span class="num">09</span><i class="rule"></i>
</section>

<!-- 12 Diamond portraits -->
<section class="slide col-l" style="top:2099px">
  <div class="photo ph-grey" role="img" aria-label="Business people working with documents at a desk"></div>
  <div class="shade" style="background:linear-gradient(90deg,rgba(20,20,22,.3),rgba(12,12,14,.8) 45%)"></div>
  <div class="brand">Oberi Investment Group</div>
  <svg width="200" height="260" style="position:absolute;left:0;top:20px" role="img" aria-label="Four diamond-framed portraits of team members">
    <g stroke="#e9a43c" stroke-width="1.5">
      <polygon points="82,10 130,58 82,106 34,58" fill="#b9a898"/>
      <polygon points="40,70 88,118 40,166 -8,118" fill="#8f8175"/>
      <polygon points="124,70 172,118 124,166 76,118" fill="#a99988"/>
      <polygon points="82,130 130,178 82,226 34,178" fill="#9b8c7e"/>
    </g>
  </svg>
  <div class="title" style="left:300px;top:55px">LOREM <em>IPSUM</em></div>
  <p class="txt" style="left:300px;top:72px;width:110px"><b>Lorem Ipsum Dolor</b>Lorem ipsum dolor sit amet, consectetuer adipiscing elit.</p>
  <p class="txt" style="left:420px;top:112px;width:110px"><b>Lorem Ipsum Dolor</b>Lorem ipsum dolor sit amet, consectetuer adipiscing elit.</p>
  <p class="txt" style="left:300px;top:158px;width:110px"><b>Lorem Ipsum Dolor</b>Lorem ipsum dolor sit amet, consectetuer adipiscing elit.</p>
  <p class="txt" style="left:420px;top:198px;width:110px"><b>Lorem Ipsum Dolor</b>Lorem ipsum dolor sit amet, consectetuer adipiscing elit.</p>
  <svg width="140" height="150" style="position:absolute;left:280px;top:76px"><g fill="#e9a43c"><circle cx="6" cy="4" r="2.5"/><circle cx="126" cy="44" r="2.5"/><circle cx="6" cy="86" r="2.5"/><circle cx="126" cy="126" r="2.5"/></g></svg>
  <p class="foot">© 2022 Copyright Oberi Investment Group - All Rights Reserved</p><span class="num">10</span><i class="rule"></i>
</section>

<!-- 13 Percentages + map -->
<section class="slide col-r" style="top:2099px">
  <div class="photo ph-city" role="img" aria-label="Aerial view of a dense city at dusk"></div>
  <div class="shade" style="background:rgba(14,16,20,.6)"></div>
  <div class="brand">Oberi Investment Group</div>
  <div class="title" style="left:30px;top:55px">LOREM <em>IPSUM</em></div>
  <svg width="60" height="200" style="position:absolute;left:28px;top:90px">
    <g fill="none" stroke-width="3">
      <circle cx="22" cy="22" r="17" stroke="rgba(255,255,255,.2)"/><circle cx="22" cy="22" r="17" stroke="#e9a43c" stroke-dasharray="32 107" transform="rotate(-90 22 22)"/>
      <circle cx="22" cy="77" r="17" stroke="rgba(255,255,255,.2)"/><circle cx="22" cy="77" r="17" stroke="#e9a43c" stroke-dasharray="53 107" transform="rotate(-90 22 77)"/>
      <circle cx="22" cy="132" r="17" stroke="rgba(255,255,255,.2)"/><circle cx="22" cy="132" r="17" stroke="#e9a43c" stroke-dasharray="86 107" transform="rotate(-90 22 132)"/>
    </g>
    <g fill="#e9a43c" font-family="Montserrat,sans-serif" font-size="8" font-weight="700" text-anchor="middle"><text x="22" y="25">30%</text><text x="22" y="80">50%</text><text x="22" y="135">80%</text></g>
  </svg>
  <p class="txt" style="left:84px;top:104px;width:90px">Lorem ipsum dolor sit amet, consectetuer adipiscing</p>
  <p class="txt" style="left:84px;top:159px;width:90px">Lorem ipsum dolor sit amet, consectetuer adipiscing</p>
  <p class="txt" style="left:84px;top:214px;width:90px">Lorem ipsum dolor sit amet, consectetuer adipiscing</p>
  <div style="position:absolute;left:220px;top:80px;width:280px;height:150px;border-radius:10px;background:linear-gradient(135deg,rgba(235,235,235,.9),rgba(200,200,200,.75))" role="img" aria-label="World map with highlighted regions in North America, Asia and Australia"></div>
  <p class="foot">© 2022 Copyright Oberi Investment Group - All Rights Reserved</p><span class="num">11</span><i class="rule"></i>
</section>

<!-- 14 Circle diagram -->
<section class="slide col-l" style="top:2440px">
  <div class="photo ph-sunset" role="img" aria-label="Office interior with large windows at sunset"></div>
  <div class="shade" style="background:rgba(12,12,14,.6)"></div>
  <div class="brand">Oberi Investment Group</div>
  <div class="title" style="left:30px;top:55px">LOREM <em>IPSUM</em></div>
  <svg width="200" height="200" style="position:absolute;left:177px;top:58px">
    <circle cx="100" cy="100" r="54" fill="#c39263" role="img" aria-label="Silhouettes of a team against a bright window"/>
    <circle cx="100" cy="100" r="70" fill="none" stroke="#e9a43c" stroke-width=".8"/>
    <g fill="#1d1d1f" stroke="#e9a43c" stroke-width="1">
      <circle cx="40" cy="64" r="9"/><circle cx="30" cy="100" r="9"/><circle cx="40" cy="136" r="9"/>
      <circle cx="160" cy="64" r="9"/><circle cx="170" cy="100" r="9"/><circle cx="160" cy="136" r="9"/>
    </g>
  </svg>
  <p class="txt" style="left:100px;top:116px;width:100px;text-align:right"><b>Lorem ipsum</b>Lorem ipsum dolor sit ametum consectetuer adipiscing elit</p>
  <p class="txt" style="left:90px;top:152px;width:100px;text-align:right"><b>Lorem ipsum</b>Lorem ipsum dolor sit ametum consectetuer adipiscing elit</p>
  <p class="txt" style="left:100px;top:188px;width:100px;text-align:right"><b>Lorem ipsum</b>Lorem ipsum dolor sit ametum consectetuer adipiscing elit</p>
  <p class="txt" style="left:358px;top:116px;width:100px"><b>Lorem ipsum</b>Lorem ipsum dolor sit ametum consectetuer adipiscing elit</p>
  <p class="txt" style="left:368px;top:152px;width:100px"><b>Lorem ipsum</b>Lorem ipsum dolor sit ametum consectetuer adipiscing elit</p>
  <p class="txt" style="left:358px;top:188px;width:100px"><b>Lorem ipsum</b>Lorem ipsum dolor sit ametum consectetuer adipiscing elit</p>
  <p class="foot">© 2022 Copyright Oberi Investment Group - All Rights Reserved</p><span class="num">12</span><i class="rule"></i>
</section>

<!-- 15 Icon tiles -->
<section class="slide col-r" style="top:2440px">
  <div class="photo ph-tower" role="img" aria-label="Skyscrapers against a blue evening sky"></div>
  <div class="shade" style="background:rgba(12,14,18,.55)"></div>
  <div class="brand">Oberi Investment Group</div>
  <div class="title" style="left:30px;top:55px">LOREM <em>IPSUM</em></div>
  <div class="tile" style="left:120px;top:82px"><svg width="20" height="20" fill="none" stroke="#e9a43c" stroke-width="1.5"><path d="M3 14l5-4 4 3 5-8"/><path d="M2 18h16"/></svg>Lorem ipsum</div>
  <div class="tile" style="left:199px;top:82px"><svg width="20" height="20" fill="none" stroke="#e9a43c" stroke-width="1.5"><rect x="2" y="5" width="16" height="12" rx="1"/><circle cx="10" cy="11" r="3.5"/></svg>Lorem ipsum</div>
  <div class="tile" style="left:278px;top:82px"><svg width="20" height="20" fill="none" stroke="#e9a43c" stroke-width="1.5"><circle cx="10" cy="10" r="8"/><path d="M7 13l2-5 4-1-2 5z"/></svg>Lorem ipsum</div>
  <div class="tile" style="left:357px;top:82px"><svg width="20" height="20" fill="none" stroke="#e9a43c" stroke-width="1.5"><path d="M1 16l6-9 4 5 3-3 5 7z"/></svg>Lorem ipsum</div>
  <div class="tile" style="left:120px;top:161px"><svg width="20" height="20" fill="none" stroke="#e9a43c" stroke-width="1.5"><rect x="2" y="3" width="16" height="14"/><path d="M2 13l5-4 4 3 7-5"/></svg>Lorem ipsum</div>
  <div class="tile" style="left:199px;top:161px"><svg width="20" height="20" fill="none" stroke="#e9a43c" stroke-width="1.5"><circle cx="6" cy="7" r="3"/><circle cx="14" cy="7" r="3"/><path d="M1 17c0-4 10-4 10 0M9 17c0-4 10-4 10 0"/></svg>Lorem ipsum</div>
  <div class="tile" style="left:278px;top:161px"><svg width="20" height="20" fill="none" stroke="#e9a43c" stroke-width="1.5"><rect x="3" y="3" width="14" height="15" rx="2"/><path d="M7 3v15M13 3v15"/></svg>Lorem ipsum</div>
  <div class="tile" style="left:357px;top:161px"><svg width="20" height="20" fill="none" stroke="#e9a43c" stroke-width="1.5"><path d="M3 3h14l-7 8z"/><path d="M10 11v7M6 18h8"/></svg>Lorem ipsum</div>
  <p class="foot">© 2022 Copyright Oberi Investment Group - All Rights Reserved</p><span class="num">13</span><i class="rule"></i>
</section>

<!-- 16 Break slide -->
<section class="slide col-l" style="top:2781px">
  <div class="photo ph-office" role="img" aria-label="Team working at a long table in a loft office"></div>
  <div class="shade" style="background:linear-gradient(90deg,rgba(10,10,12,.7),rgba(10,10,12,.25))"></div>
  <div class="brand">Oberi Investment Group</div>
  <div style="position:absolute;left:30px;top:222px;font-weight:800;font-size:27px;color:var(--white)">BREAK <span class="gold">SLIDE</span></div>
  <p class="foot">© 2022 Copyright Oberi Investment Group - All Rights Reserved</p><span class="num">14</span><i class="rule"></i>
</section>

<!-- 17 Three cards -->
<section class="slide col-r" style="top:2781px;background:linear-gradient(180deg,#2b2d31,#131314)">
  <div class="photo ph-tower" style="bottom:150px" role="img" aria-label="Handshake in front of a city skyline"></div>
  <div class="brand">Oberi Investment Group</div>
  <div style="position:absolute;left:0;right:0;top:72px;text-align:center;font-weight:700;font-size:16px;color:var(--white)">LOREM <span class="gold">IPSUM</span></div>
  <div class="card" style="left:72px;top:126px;width:112px;height:118px"></div>
  <div class="card" style="left:221px;top:126px;width:112px;height:118px"></div>
  <div class="card" style="left:370px;top:126px;width:112px;height:118px"></div>
  <svg width="554" height="40" style="position:absolute;left:0;top:126px"><g fill="#e9a43c"><circle cx="128" cy="17" r="11"/><circle cx="277" cy="17" r="11"/><circle cx="426" cy="17" r="11"/></g><g fill="none" stroke="#fff" stroke-width="1.2"><circle cx="128" cy="17" r="5"/><rect x="272" y="12" width="10" height="10"/><path d="M422 22l8-10"/></g></svg>
  <p class="txt" style="left:80px;top:162px;width:96px;text-align:center">Lorem ipsum dolor sit amet, consectetuer adipiscing elit, sed diam nonummy nibh eui tincidunt ut laoreet dolore magna aliquam volutpat. Ut wisi enim ad</p>
  <p class="txt" style="left:229px;top:162px;width:96px;text-align:center">Lorem ipsum dolor sit amet, consectetuer adipiscing elit, sed diam nonummy nibh eui tincidunt ut laoreet dolore magna aliquam volutpat. Ut wisi enim ad</p>
  <p class="txt" style="left:378px;top:162px;width:96px;text-align:center">Lorem ipsum dolor sit amet, consectetuer adipiscing elit, sed diam nonummy nibh eui tincidunt ut laoreet dolore magna aliquam volutpat. Ut wisi enim ad</p>
  <div class="dots" style="position:absolute;left:116px;top:226px">•••</div>
  <div class="dots" style="position:absolute;left:265px;top:226px">•••</div>
  <div class="dots" style="position:absolute;left:414px;top:226px">•••</div>
  <p class="foot">© 2022 Copyright Oberi Investment Group - All Rights Reserved</p><span class="num">15</span><i class="rule"></i>
</section>

<!-- 18 Hexagons -->
<section class="slide col-l" style="top:3122px">
  <div class="photo ph-office" role="img" aria-label="Two businessmen meeting in an office"></div>
  <div class="shade" style="background:rgba(12,12,14,.55)"></div>
  <div class="brand">Oberi Investment Group</div>
  <div class="title" style="left:30px;top:55px">LOREM <em>IPSUM</em></div>
  <svg width="554" height="160" style="position:absolute;left:0;top:90px">
    <g stroke="#e9a43c" stroke-width=".6" fill="none"><path d="M150 64v56M200 64v46M250 64v56M300 64v46M350 64v56M400 64v46"/></g>
    <g>
      <polygon points="150,14 176,29 176,59 150,74 124,59 124,29" fill="#e9a43c"/>
      <polygon points="200,14 226,29 226,59 200,74 174,59 174,29" fill="#2a2b2e"/>
      <polygon points="250,14 276,29 276,59 250,74 224,59 224,29" fill="#e9a43c"/>
      <polygon points="300,14 326,29 326,59 300,74 274,59 274,29" fill="#2a2b2e"/>
      <polygon points="350,14 376,29 376,59 350,74 324,59 324,29" fill="#e9a43c"/>
      <polygon points="400,14 426,29 426,59 400,74 374,59 374,29" fill="#2a2b2e"/>
    </g>
    <g fill="none" stroke="#fff" stroke-width="1.2">
      <rect x="143" y="37" width="14" height="14"/><rect x="193" y="37" width="14" height="12" rx="1"/><path d="M243 48l14-8-14-6"/>
      <circle cx="300" cy="44" r="7"/><path d="M343 38h14v6q0 7-7 9q-7-2-7-9z"/><path d="M393 46q7-10 14 0"/>
    </g>
  </svg>
  <p class="txt" style="left:120px;top:212px;width:60px;text-align:center">Lorem ipsum dolor sit amet</p>
  <p class="txt" style="left:170px;top:202px;width:60px;text-align:center">Lorem ipsum dolor sit amet</p>
  <p class="txt" style="left:220px;top:212px;width:60px;text-align:center">Lorem ipsum dolor sit amet</p>
  <p class="txt" style="left:270px;top:202px;width:60px;text-align:center">Lorem ipsum dolor sit amet</p>
  <p class="txt" style="left:320px;top:212px;width:60px;text-align:center">Lorem ipsum dolor sit amet</p>
  <p class="txt" style="left:370px;top:202px;width:60px;text-align:center">Lorem ipsum dolor sit amet</p>
  <p class="foot">© 2022 Copyright Oberi Investment Group - All Rights Reserved</p><span class="num">16</span><i class="rule"></i>
</section>

<!-- 19 Icon points -->
<section class="slide col-r" style="top:3122px;background:linear-gradient(180deg,#1a1b1d,#2a2b2e)">
  <div class="photo" style="background:radial-gradient(ellipse at 50% 40%,rgba(255,255,255,.07),transparent 60%)" role="img" aria-label="Faint world map in the background"></div>
  <div class="brand">Oberi Investment Group</div>
  <div class="title" style="left:30px;top:55px">LOREM <em>IPSUM</em></div>
  <svg width="554" height="160" style="position:absolute;left:0;top:100px">
    <g fill="#2e2f33" stroke="#e9a43c" stroke-width="2"><circle cx="70" cy="26" r="14"/><circle cx="228" cy="26" r="14"/><circle cx="386" cy="26" r="14"/><circle cx="148" cy="88" r="14"/><circle cx="306" cy="88" r="14"/></g>
    <g fill="none" stroke="#e9a43c" stroke-width="1.2"><circle cx="70" cy="26" r="5"/><rect x="223" y="21" width="10" height="10" rx="2"/><path d="M381 31v-10M386 31v-7M391 31v-4"/><path d="M143 92v-8l10-2v8"/><circle cx="306" cy="88" r="6"/><path d="M306 84v4h3"/></g>
  </svg>
  <p class="txt" style="left:94px;top:112px;width:100px"><b>Lorem ipsum</b>Lorem ipsum dolor sit amet, ametum consectetuer adipiscing elit sedu diam</p>
  <p class="txt" style="left:252px;top:112px;width:100px"><b>Lorem ipsum</b>Lorem ipsum dolor sit amet, ametum consectetuer adipiscing elit sedu diam</p>
  <p class="txt" style="left:410px;top:112px;width:100px"><b>Lorem ipsum</b>Lorem ipsum dolor sit amet, ametum consectetuer adipiscing elit sedu diam</p>
  <p class="txt" style="left:172px;top:174px;width:100px"><b>Lorem ipsum</b>Lorem ipsum dolor sit amet, ametum consectetuer adipiscing elit sedu diam</p>
  <p class="txt" style="left:330px;top:174px;width:100px"><b>Lorem ipsum</b>Lorem ipsum dolor sit amet, ametum consectetuer adipiscing elit sedu diam</p>
  <p class="foot">© 2022 Copyright Oberi Investment Group - All Rights Reserved</p><span class="num">17</span><i class="rule"></i>
</section>

<!-- 20 Table -->
<section class="slide col-l" style="top:3463px">
  <div class="photo ph-warm" role="img" aria-label="Modern office building entrance with people walking"></div>
  <div class="shade" style="background:rgba(12,12,14,.55)"></div>
  <div class="brand">Oberi Investment Group</div>
  <div class="title" style="left:30px;top:88px">LOREM <em>IPSUM</em></div>
  <p class="txt" style="left:30px;top:106px;width:150px">Lorem ipsum dolor sit amet, consectetuer adipiscing elit, sed diam nonummy nibh euismod tincidunt ut laoreet dolore magna aliquam erat volutpat. Ut wisi enim ad minim veniam, quis nostrud exerci tation ullamcorper suscipit lobortis nisl ut aliquip ex ea commodo consequat. Duis autem vel eum iriure.</p>
  <table class="grid" style="left:210px;top:82px;width:316px">
    <tr><th>Lorem ipsum</th><th>Column 1</th><th>Column 2</th><th>Column 3</th></tr>
    <tr><td>Lorem ipsum</td><td>Lorem ipsum</td><td>Lorem ipsum</td><td>Lorem ipsum</td></tr>
    <tr><td>Lorem ipsum</td><td>Lorem ipsum</td><td>Lorem ipsum</td><td>Lorem ipsum</td></tr>
    <tr><td>Lorem ipsum</td><td>Lorem ipsum</td><td>Lorem ipsum</td><td>Lorem ipsum</td></tr>
    <tr><td>Lorem ipsum</td><td>Lorem ipsum</td><td>Lorem ipsum</td><td>Lorem ipsum</td></tr>
    <tr><td>Lorem ipsum</td><td>Lorem ipsum</td><td>Lorem ipsum</td><td>Lorem ipsum</td></tr>
    <tr><td>Lorem ipsum</td><td>Lorem ipsum</td><td>Lorem ipsum</td><td>Lorem ipsum</td></tr>
  </table>
  <p class="foot">© 2022 Copyright Oberi Investment Group - All Rights Reserved</p><span class="num">18</span><i class="rule"></i>
</section>

<!-- 21 Stats + bar chart -->
<section class="slide col-r" style="top:3463px">
  <div class="photo ph-cool" role="img" aria-label="Business people walking in a bright city street"></div>
  <div class="shade" style="background:linear-gradient(90deg,rgba(20,22,26,.75),rgba(20,22,26,.35))"></div>
  <div class="brand">Oberi Investment Group</div>
  <div class="title" style="left:30px;top:88px">LOREM <em>IPSUM</em></div>
  <p class="txt" style="left:30px;top:104px;width:260px">Lorem ipsum dolor sit amet, consectetuer adipiscing elit, sed diam nonummy nibh euismod tincidunt ut laoreet dolore magna aliquam erat volutpat. Ut wisi enim ad minim veniam, quis nostrud exerci tation ullamcorper suscipit.</p>
  <div style="position:absolute;left:36px;top:146px;font-weight:700;font-size:12px">3.5M</div>
  <div style="position:absolute;left:112px;top:146px;font-weight:700;font-size:12px">5.6M</div>
  <div style="position:absolute;left:188px;top:146px;font-weight:700;font-size:12px">6.8M</div>
  <p class="txt" style="left:36px;top:162px;width:60px">Lorem ipsum dolor sit amet, consectetu adipiscing elit, sed di nonummy nibh</p>
  <p class="txt" style="left:112px;top:162px;width:60px;padding-left:4px;border-left:1px solid var(--gold)">Lorem ipsum dolor sit amet, consectetu adipiscing elit, sed di nonummy nibh</p>
  <p class="txt" style="left:188px;top:162px;width:60px;padding-left:4px;border-left:1px solid var(--gold)">Lorem ipsum dolor sit amet, consectetu adipiscing elit, sed di nonummy nibh</p>
  <svg width="220" height="190" style="position:absolute;left:320px;top:70px">
    <defs><linearGradient id="bar" x1="0" y1="0" x2="0" y2="1"><stop offset="0" stop-color="#f3bd5c"/><stop offset="1" stop-color="#c57f22"/></linearGradient></defs>
    <g fill="#fff" font-family="Montserrat,sans-serif" font-size="4.5" text-anchor="end"><text x="14" y="12">100</text><text x="14" y="42">80</text><text x="14" y="72">60</text><text x="14" y="102">40</text><text x="14" y="132">20</text><text x="14" y="162">0</text></g>
    <g fill="url(#bar)">
      <rect x="24" y="70" width="8" height="90"/><rect x="35" y="100" width="8" height="60"/><rect x="46" y="60" width="8" height="100"/>
      <rect x="72" y="90" width="8" height="70"/><rect x="83" y="50" width="8" height="110"/><rect x="94" y="80" width="8" height="80"/>
      <rect x="120" y="40" width="8" height="120"/><rect x="131" y="75" width="8" height="85"/><rect x="142" y="95" width="8" height="65"/>
      <rect x="168" y="30" width="8" height="130"/><rect x="179" y="65" width="8" height="95"/><rect x="190" y="15" width="8" height="145"/>
    </g>
    <line x1="18" y1="160" x2="208" y2="160" stroke="#fff" stroke-width=".5"/>
    <g fill="#fff" font-family="Montserrat,sans-serif" font-size="4.5" text-anchor="middle"><text x="39" y="170">Lorem ipsum</text><text x="87" y="170">Lorem ipsum</text><text x="135" y="170">Lorem ipsum</text><text x="183" y="170">Lorem ipsum</text></g>
  </svg>
  <p class="foot">© 2022 Copyright Oberi Investment Group - All Rights Reserved</p><span class="num">19</span><i class="rule"></i>
</section>

<!-- 22 Icon library -->
<section class="slide col-l" style="top:3804px;background:var(--white)">
  <svg width="480" height="210" style="position:absolute;left:37px;top:48px">
    <defs>
      <pattern id="icons" width="27" height="21" patternUnits="userSpaceOnUse">
        <g fill="none" stroke="#e9a43c" stroke-width="1">
          <circle cx="6" cy="6" r="3.5"/>
          <rect x="16" y="2.5" width="7" height="7" rx="1"/>
          <path d="M2 18l4-5 4 5z"/>
          <path d="M16 14h7M16 17h7M19.5 12v8"/>
        </g>
      </pattern>
    </defs>
    <rect width="480" height="210" fill="url(#icons)"/>
  </svg>
  <p class="foot" style="color:#999">© 2022 Copyright Oberi Investment Group - All Rights Reserved</p><span class="num" style="color:#999">20</span><i class="rule"></i>
</section>

<!-- 23 Contact -->
<section class="slide col-r" style="top:3804px">
  <div class="photo ph-grey" role="img" aria-label="Monochrome handshake over a city skyline"></div>
  <div class="shade" style="background:rgba(16,16,18,.5)"></div>
  <div class="brand mid" style="top:90px">Oberi Investment Group</div>
  <div style="position:absolute;left:212px;top:138px;font-weight:700;font-size:17px;color:var(--white)">CONTACT US</div>
  <svg width="14" height="70" style="position:absolute;left:212px;top:162px">
    <g fill="none" stroke="#e9a43c" stroke-width="1"><rect x="1" y="2" width="10" height="7"/><path d="M1 2l5 4 5-4"/><path d="M6 26c-3-3-4-5-4-7a4 4 0 018 0c0 2-1 4-4 7z"/><circle cx="6" cy="36" r="5"/><path d="M1 36h10M6 31v10"/><path d="M3 48q0 5 6 6l2-2-2-2-1 1q-2-1-3-3l1-1-2-2z"/></g>
  </svg>
  <p class="txt" style="left:228px;top:162px;line-height:2.05;font-size:5.5px">Lorem Ipsum Dolor Sit Amet<br>Lorem Ipsum Dolor Sit Amet<br>Lorem Ipsum Dolor Sit Amet<br>Lorem Ipsum Dolor Sit Amet</p>
  <svg width="60" height="16" style="position:absolute;left:240px;top:220px"><g fill="#e9a43c"><circle cx="8" cy="8" r="7"/><circle cx="28" cy="8" r="7"/><circle cx="48" cy="8" r="7"/></g></svg>
  <p class="foot">© 2022 Copyright Oberi Investment Group - All Rights Reserved</p><span class="num">21</span><i class="rule"></i>
</section>

</body>
</html>
```